La etiqueta deberá contener lo siguiente:
-Titulo: Miel de Agave Kosher
-Logo de VORET (realizado por ustedes, adjunto diseño)
-Logo del certificado: KOSHER (Se adjuntan certificado)
-Mililitros: 750 ml
-Información nutrimental: se adjunta tabla
La miel deberá sobresalir de las demás por el estilo lujoso y llamativo de la etiqueta.

```html
<!DOCTYPE html>
<html lang="es">
<head>
<meta charset="UTF-8">
<title>VORET · Miel de Agave Kosher · Etiquetas</title>
<link rel="stylesheet" href="https://fonts.googleapis.com/css2?family=Barlow+Condensed:wght@300;400;500;600;700&display=swap">
<style>
  :root {
    --bg: #efefef;
    --label: #050505;
    --ink-light: #f2f2f2;
    --ink-grey: #b9b9b9;
    --hex-line: #8a8a8a;
    --gold: #c9a227;
    --gold-dark: #8f6f12;
  }
  * { margin: 0; padding: 0; box-sizing: border-box; }
  html, body {
    width: 1200px; height: 1058px; overflow: hidden;
    background: var(--bg);
    font-family: "Barlow Condensed", "Arial Narrow", sans-serif;
  }
  .canvas {
    position: relative; width: 1200px; height: 1058px;
  }
  .label {
    position: absolute; top: 331px;
    width: 365px; height: 396px;
    background: var(--label);
    color: var(--ink-light);
  }
  .label--front { left: 215px; }
  .label--back { left: 620px; }

  .hexagon-frame { position: absolute; inset: 0; }

  .brand {
    position: absolute; left: 0; right: 0; top: 64px;
    display: flex; flex-direction: column; align-items: center; gap: 12px;
  }
  .brand-mark {
    width: 28px; height: 28px; border-radius: 50%;
    border: 2.5px solid var(--gold);
  }
  .brand-name {
    font-weight: 600; font-size: 20px; letter-spacing: 4px;
    color: var(--ink-grey);
  }
  .product-title {
    position: absolute; left: 0; right: 0; top: 162px;
    text-align: center;
    font-weight: 300; font-size: 45px; letter-spacing: 0.5px; line-height: 1;
  }
  .title-rule {
    position: absolute; left: 79px; width: 210px; top: 211px;
    height: 1.5px; background: var(--gold);
  }
  .product-subtitle {
    position: absolute; left: 0; right: 0; top: 220px;
    text-align: center;
    font-weight: 400; font-size: 22px; letter-spacing: 4px; line-height: 1;
    color: #d8d8d8;
  }
  .volume {
    position: absolute; left: 0; right: 0; top: 364px;
    text-align: center;
    font-weight: 400; font-size: 22px; letter-spacing: 0.5px; line-height: 1;
    color: #d8d8d8;
  }

  .nutrition-panel {
    position: absolute; left: 101px; top: 44px;
    width: 156px; height: 220px;
    border: 2px solid var(--ink-light); border-radius: 10px;
    padding: 14px 10px 8px;
  }
  .nutrition-title {
    text-align: center; font-weight: 700; font-size: 11.5px;
    line-height: 1.05; letter-spacing: 0.3px; margin-bottom: 12px;
  }
  .nutrition-table { font-size: 5.6px; line-height: 1.35; }
  .nutrition-row {
    display: flex; justify-content: space-between; gap: 4px;
  }
  .nutrition-row--ruled { border-bottom: 0.8px solid var(--ink-light); padding-bottom: 1px; margin-bottom: 1.5px; }
  .nutrition-row--thick { border-bottom: 2px solid var(--ink-light); padding-bottom: 2px; margin-bottom: 4px; }
  .nutrition-row--indent { padding-left: 20px; }
  .nutrition-row strong { font-weight: 700; }
  .nutrition-value { text-align: right; }

  .certificate-seal {
    position: absolute; left: 144px; top: 313px;
    width: 62px; height: 62px; border-radius: 50%;
    background: radial-gradient(circle, var(--gold) 55%, var(--gold-dark) 100%);
  }
</style>
</head>
<body>
<main class="canvas">

  <section class="label label--front">
    <svg class="hexagon-frame" width="365" height="396" viewBox="0 0 365 396" aria-hidden="true">
      <polygon points="184,23 322,100 322,276 184,353 46,276 46,100"
               fill="none" stroke="var(--hex-line)" stroke-width="1"/>
    </svg>
    <div class="brand">
      <span class="brand-mark"></span>
      <span class="brand-name">VORET</span>
    </div>
    <h1 class="product-title">MIEL DE AGAVE</h1>
    <div class="title-rule"></div>
    <p class="product-subtitle">KOSHER</p>
    <p class="volume">750ML</p>
  </section>

  <section class="label label--back">
    <div class="nutrition-panel">
      <h2 class="nutrition-title">DECLARACIÓN<br>NUTRIMENTAL</h2>
      <div class="nutrition-table">
        <div class="nutrition-row nutrition-row--thick"><span>Contenido energético por envase</span><span class="nutrition-value">2,050 kcal<br>8,639 kJ</span></div>
        <div class="nutrition-row"><span>Tamaño de la porción</span><span>100g</span></div>
        <div class="nutrition-row"><span>Porciones por envase</span><span>3.3</span></div>
        <div class="nutrition-row nutrition-row--thick"><strong>Contenido energético por porción</strong><span class="nutrition-value">310 kcal<br>1,309 kJ</span></div>
        <div class="nutrition-row nutrition-row--ruled"><strong>Proteínas</strong><span>0 g</span></div>
        <div class="nutrition-row nutrition-row--ruled"><span>Grasas</span><span>0 g</span></div>
        <div class="nutrition-row nutrition-row--ruled nutrition-row--indent"><strong>Grasa saturada</strong><span>0 mg</span></div>
        <div class="nutrition-row nutrition-row--ruled nutrition-row--indent"><strong>Grasas trans</strong><span>0 mg</span></div>
        <div class="nutrition-row nutrition-row--ruled"><span>Hidratos de carbono disponibles</span><span>77 g</span></div>
        <div class="nutrition-row nutrition-row--ruled nutrition-row--indent"><span>Azúcares</span><span>77 g</span></div>
        <div class="nutrition-row nutrition-row--ruled nutrition-row--indent"><strong>Azúcares añadidos</strong><span>0 g</span></div>
        <div class="nutrition-row nutrition-row--ruled"><span>Fibra dietética</span><span>menos de 1 g</span></div>
        <div class="nutrition-row"><strong>Sodio</strong><span>0 mg</span></div>
      </div>
    </div>
    <div class="certificate-seal" role="img" aria-label="Sello de certificación kosher"></div>
  </section>

</main>
</body>
</html>
```